Wellness Company needs 2 updated pages for our powerpoint

1 page of our powerpoint needs to be split into 2 pages. I have uploaded an image of it all on 1 page, the left side needs to be on 1 page and the right side needs to be on a separate page. I also uploaded images of the top & bottom since it is so blurry. Landscape view, please. Don't worry about the bottom of the page design since that is our template.

Target Market(s)

Wellness and Business

Industry/Entity Type

Health And Wellness

Requirements
Must have
• Clear wording and bold font.
Nice to have
• Clear circles and images

```html
<!DOCTYPE html>
<html lang="en">
<head>
<meta charset="utf-8">
<title>Leafline Wellness – Compensation Plan at a Glance</title>
<link href="https://fonts.googleapis.com/css2?family=Comfortaa:wght@400;700&family=Signika:wght@400;600&family=Open+Sans:wght@400;600;700&display=swap" rel="stylesheet">
<style>
  :root{
    --green:#6aa81e;
    --green-dark:#5a9616;
    --orange:#f0a81c;
    --grey:#8a8a8a;
    --grey-light:#c9c9c9;
    --text:#555;
    --paper:#ffffff;
  }
  *{margin:0;padding:0;box-sizing:border-box}
  html,body{width:1200px;height:880px;overflow:hidden;background:var(--paper)}
  .canvas{position:relative;width:1200px;height:880px;font-family:"Open Sans",sans-serif;color:var(--text)}
  .shapes{position:absolute;left:0;top:0}
  .abs{position:absolute;white-space:nowrap}

  .header-label{font-family:"Comfortaa",sans-serif;font-size:21px;color:var(--orange);top:103px}
  .brand-name{font-family:"Signika",sans-serif;font-weight:600;color:var(--green);font-size:24px;line-height:28px;text-align:center;left:220px;width:174px;top:92px;white-space:normal;letter-spacing:.5px}

  .panel-title{font-family:"Signika",sans-serif;font-size:18px;color:var(--green);border-bottom:1.5px solid var(--green);line-height:22px;padding-bottom:1px}
  .lead{font-size:12.5px;color:var(--orange)}

  .price-row{font-size:14px;color:var(--text);left:60px;width:158px;display:flex;justify-content:space-between}
  .price-row.rule{border-bottom:1.5px solid var(--green);padding-bottom:1px}

  .caption{font-size:12px;line-height:17px;text-align:center;color:var(--text);white-space:normal}
  .bonus-note{font-size:11.2px;line-height:15.5px;text-align:center;white-space:normal;color:var(--text)}

  .col-head{font-family:"Signika",sans-serif;font-size:18px;color:var(--orange);text-align:center;width:104px;top:134px}
  .level{font-family:"Signika",sans-serif;font-size:15px;color:var(--orange);left:683px}
  .rate{font-family:"Signika",sans-serif;font-size:18px;color:#fff;text-align:center;width:104px}

  .rank-notes{left:635px;top:363px;font-size:10.5px;line-height:15px;color:var(--green-dark)}

  .quals-title{left:878px;top:441px;font-family:"Open Sans",sans-serif;font-weight:700;font-size:14px;color:var(--green);border-bottom:1.5px solid var(--green);line-height:18px}
  .quals{left:689px;top:481px;font-size:10px;line-height:14px;color:var(--green-dark);list-style:none}
  .quals li{margin-bottom:5px}
  .quals .req{padding-left:13px}
  .fine-print{left:684px;top:774px;font-size:7.5px;line-height:14px;color:var(--green-dark)}
</style>
</head>
<body>
<div class="canvas">

  <svg class="shapes" width="1200" height="880" viewBox="0 0 1200 880" aria-hidden="true">
    <!-- header frame -->
    <path d="M34,98 H220 V62 H394 V98 H576 V134 H394 V179 H220 V134 H34 Z" fill="none" stroke="var(--green)" stroke-width="2.5"/>
    <circle cx="248" cy="92" r="0" fill="none"/>

    <!-- panel frames -->
    <rect x="36" y="234" width="249" height="196" fill="none" stroke="var(--green)" stroke-width="5"/>
    <rect x="328" y="234" width="249" height="196" fill="none" stroke="var(--green)" stroke-width="5"/>
    <rect x="36" y="452" width="537" height="345" fill="none" stroke="var(--green)" stroke-width="5"/>
    <rect x="615" y="65" width="550" height="367" fill="none" stroke="var(--green)" stroke-width="5"/>

    <!-- step number rings -->
    <g fill="none" stroke="var(--green)" stroke-width="1.8">
      <circle cx="68" cy="264" r="18"/>
      <circle cx="365" cy="266" r="18"/>
      <circle cx="306" cy="490" r="18"/>
      <circle cx="645" cy="102" r="18"/>
    </g>
    <g font-family="Comfortaa, sans-serif" font-size="27" fill="var(--green)" text-anchor="middle">
      <text x="68" y="274">1</text>
      <text x="365" y="276">2</text>
      <text x="306" y="500">3</text>
      <text x="645" y="112">4</text>
    </g>

    <!-- fast start tree -->
    <g stroke="var(--orange)" stroke-width="4" fill="none">
      <line x1="451" y1="307" x2="396" y2="334"/>
      <line x1="451" y1="307" x2="452" y2="334"/>
      <line x1="451" y1="307" x2="509" y2="334"/>
    </g>
    <g fill="#fff" stroke="var(--orange)" stroke-width="2.5">
      <circle cx="451" cy="288" r="19"/>
      <circle cx="396" cy="353" r="19"/>
      <circle cx="452" cy="353" r="19"/>
      <circle cx="509" cy="353" r="19"/>
    </g>
    <g font-family="Open Sans, sans-serif" font-size="13.5" text-anchor="middle">
      <text x="451" y="293" fill="var(--orange)">You</text>
      <text x="396" y="358" fill="var(--grey)">$10</text>
      <text x="452" y="358" fill="var(--orange)">$20</text>
      <text x="509" y="358" fill="var(--grey-light)">$40</text>
    </g>

    <!-- leadership trees -->
    <g stroke="var(--orange)" stroke-width="4" fill="none">
      <line x1="129" y1="578" x2="71" y2="607"/><line x1="129" y1="578" x2="129" y2="607"/><line x1="129" y1="578" x2="186" y2="607"/>
      <line x1="306" y1="578" x2="249" y2="607"/><line x1="306" y1="578" x2="306" y2="607"/><line x1="306" y1="578" x2="363" y2="607"/>
      <line x1="486" y1="578" x2="429" y2="607"/><line x1="486" y1="578" x2="486" y2="607"/><line x1="486" y1="578" x2="543" y2="607"/>
    </g>
    <g fill="#fff" stroke="var(--orange)" stroke-width="2.5">
      <circle cx="129" cy="559" r="19"/><circle cx="71" cy="626" r="19"/><circle cx="129" cy="626" r="19"/><circle cx="186" cy="626" r="19"/>
      <circle cx="306" cy="559" r="19"/><circle cx="249" cy="626" r="19"/><circle cx="306" cy="626" r="19"/><circle cx="363" cy="626" r="19"/>
      <circle cx="486" cy="559" r="19"/><circle cx="429" cy="626" r="19"/><circle cx="486" cy="626" r="19"/><circle cx="543" cy="626" r="19"/>
    </g>
    <g font-family="Open Sans, sans-serif" font-size="12" font-weight="700" text-anchor="middle" fill="var(--orange)">
      <text x="129" y="563">MBO</text><text x="306" y="563">SBO</text><text x="486" y="563">EBO</text>
    </g>
    <g font-family="Open Sans, sans-serif" font-size="13.5" text-anchor="middle">
      <text x="71" y="631" fill="var(--grey)">$10</text><text x="129" y="631" fill="var(--orange)">$20</text><text x="186" y="631" fill="var(--grey-light)">$40</text>
      <text x="249" y="631" fill="var(--grey)">$20</text><text x="306" y="631" fill="var(--orange)">$40</text><text x="363" y="631" fill="var(--grey-light)">$80</text>
      <text x="429" y="631" fill="var(--grey)">$40</text><text x="486" y="631" fill="var(--orange)">$80</text><text x="543" y="631" fill="var(--grey-light)">$160</text>
    </g>
    <g stroke="var(--grey-light)" stroke-width="1">
      <line x1="206" y1="656" x2="206" y2="794"/>
      <line x1="390" y1="656" x2="390" y2="794"/>
    </g>

    <!-- unilevel table -->
    <g stroke="var(--orange)" stroke-width="1">
      <line x1="678" y1="186" x2="1116" y2="186"/>
      <line x1="678" y1="207" x2="1116" y2="207"/>
      <line x1="678" y1="230" x2="1116" y2="230"/>
      <line x1="678" y1="252" x2="1116" y2="252"/>
      <line x1="678" y1="275" x2="1116" y2="275"/>
      <line x1="678" y1="298" x2="1116" y2="298"/>
      <line x1="678" y1="320" x2="1116" y2="320"/>
      <line x1="678" y1="344" x2="1116" y2="344"/>
      <line x1="698" y1="164" x2="698" y2="344"/>
    </g>
    <rect x="698" y="164" width="103" height="43" fill="var(--green)"/>
    <rect x="804" y="164" width="102" height="88" fill="var(--green)"/>
    <rect x="909" y="164" width="101" height="134" fill="var(--green)"/>
    <rect x="1014" y="164" width="101" height="156" fill="var(--green)"/>
    <rect x="1014" y="322" width="101" height="22" fill="var(--orange)"/>
  </svg>

  <!-- header -->
  <div class="abs header-label" style="left:38px">Compensation Plan</div>
  <div class="abs header-label" style="left:430px">At a Glance</div>
  <div class="abs brand-name">Leafline Wellness</div>

  <!-- 1 direct selling -->
  <div class="abs panel-title" style="left:110px;top:260px">Direct Selling</div>
  <div class="abs lead" style="left:59px;top:296px">Sell the product. Keep the profit.</div>
  <div class="abs price-row" style="top:329px"><span>Suggested Retail:</span><span>$34.95</span></div>
  <div class="abs price-row rule" style="top:352px"><span>Wholesale:</span><span>$24.95</span></div>
  <div class="abs price-row" style="top:375px"><span>You keep</span><span>$10.00</span></div>

  <!-- 2 fast start -->
  <div class="abs panel-title" style="left:390px;top:240px">Fast Start Bonus</div>
  <div class="abs caption" style="left:336px;width:236px;top:384px">Earn up to $40 for each silver, gold or platinum package you sell</div>

  <!-- 3 leadership -->
  <div class="abs panel-title" style="left:235px;top:510px">Leadership Bonus</div>
  <div class="abs bonus-note" style="left:56px;width:146px;top:673px">MBO earn up to $10. $20 or $40 per enrollment package sold.</div>
  <div class="abs bonus-note" style="left:228px;width:156px;top:676px">SBO earn up to $20, $40 or $80 for every enrollment package sold. SBO between different leaders. MBOs and SBOs will split the the difference between bonuses.</div>
  <div class="abs bonus-note" style="left:400px;width:172px;top:673px">SBO earn up to $40, $80 or $160 for every enrollment package sold. EBO leadership bonus can be split between leaders. MBOs, SBOs and EBOs will split the the difference between bonuses.</div>

  <!-- 4 unilevel -->
  <div class="abs panel-title" style="left:814px;top:88px">Unilevel Commission</div>
  <div class="abs col-head" style="left:698px">IBO</div>
  <div class="abs col-head" style="left:802px">MBO</div>
  <div class="abs col-head" style="left:906px">SBO</div>
  <div class="abs col-head" style="left:1010px">EBO/REBO</div>

  <div class="abs level" style="top:164px">1</div>
  <div class="abs level" style="top:187px">2</div>
  <div class="abs level" style="top:209px">3</div>
  <div class="abs level" style="top:232px">4</div>
  <div class="abs level" style="top:255px">5</div>
  <div class="abs level" style="top:277px">6</div>
  <div class="abs level" style="top:300px">7</div>
  <div class="abs level" style="top:323px">8</div>

  <div class="abs rate" style="left:698px;top:175px">5%</div>
  <div class="abs rate" style="left:803px;top:198px">5%</div>
  <div class="abs rate" style="left:908px;top:224px">5%</div>
  <div class="abs rate" style="left:1013px;top:237px">5%</div>
  <div class="abs rate" style="left:1013px;top:322px">10%</div>

  <div class="abs rank-notes">
    IBOs earn 5% commission on all sales 2 levels deep.<br>
    MBOs earn 5% commission on all sales 4 levels deep.<br>
    SBOs earn 5% commission on all sales 6 levels deep.<br>
    EBOs earn 5% commission on all sales 7 levels deep and 10% on the 8th level.
  </div>

  <!-- qualifications -->
  <div class="abs quals-title">Qualifications</div>
  <ol class="abs quals">
    <li>1. Independent Business Owner(IBO)
      <div class="req">-Enroll as an Active Independent Business Owner</div>
      <div class="req">-After your first month to remain active you must personally maintain a minimum of<br>&nbsp;25 business volume &amp; subscribe to autoship.</div></li>
    <li>2. Managing Business Owner(MBO)
      <div class="req">-Be an Active IBO and personally maintain 50 business volume</div>
      <div class="req">-Personally Sponsor 3 IBO’s. Each of them must be active.</div></li>
    <li>3. Senior Business Owner(SBO)
      <div class="req">-Be an Active IBO and personally acquire 100 business volume</div>
      <div class="req">-Promote 3 MBO’s in 3 Separate Legs</div>
      <div class="req">-Maintain 1500 combined business volume for entire downline</div></li>
    <li>4. Executive Business Owner(EBO)
      <div class="req">-Be an Active IBO and personally maintain 200 business volume</div>
      <div class="req">-Promote 3 SBO’s in 3 Separate Legs</div>
      <div class="req">-Maintain 5000 combined business volume for entire downline</div></li>
    <li>5. Regional Executive Business Owner(REBO)
      <div class="req">-Be an Active IBO and personally maintain 400 business volume</div>
      <div class="req">-Promote 3 EBO’s in 3 Separate Legs</div>
      <div class="req">-Maintain 15000 combined business volume for entire downline</div></li>
  </ol>
  <div class="abs fine-print">*All requirements must be met to stay commissionable within that rank<br>This is an example only, see full comp plan for details.</div>

</div>
</body>
</html>
```